Premium CBD/Hemp company needs packaging and label design

Verdant Oakfield, a premium CBD/Hemp company based in Scottsdale, Arizona is in need of a packaging and label design. We are launching with our flagship product which will be a 30 count capsule and will come in three functions: Pain Relief, Anxiety Support, and Sleep Support. For the purpose of this contest, please design packaging and label for our Anxiety Support product. Our products are physician formulated and all natural. Our main ingredient is CBD/Hemp and is complemented by specific herbs that synergistically work together to give the customer the most effective and desired result. We would like our branding to have a pharmaceutical look and feel with a focus on trust and transparency. We have uploaded our company logo that is to be used on both the packaging and label. We have also uploaded an executed branding questionnaire that will guide you to exactly what we are seeking to achieve as to the look and feel of our brand. Please feel free to contact us with any questions that you may have. The winner of this contest will have the opportunity to work with us on future projects as we will need packaging and label design for our entire Verdant Oakfield product line.

Target Market(s)

See attached branding questionnaire

Industry/Entity Type

Health And Wellness

Font styles to use
Sans Serif

Colors

Designer to choose colors to be used in the design.

Requirements
Must have
• See attached branding questionnaire; Please superimpose labels onto a cobalt blue capsule bottle (see attached)
• >>UPON REVIEW of the FIRST 8 designs, we really like the silver, mildly metallic label background in DESIGN # 21300528, we do not want metalic lettering as that would not look very "Pharmaceutical"
• >>We are in search of a look that is a bit more "Pharmaceutical" than a look that would be more commonly found in a Supplement Store
Nice to have
• "See attached branding questionnaire
Should not have
• See attached branding questionnaire; NO marijuana or cannabis plant on the packaging or label

```html
<!DOCTYPE html>
<html lang="en">
<head>
<meta charset="utf-8">
<title>Verdant Oakfield – Anxiety Support Packaging</title>
<link href="https://fonts.googleapis.com/css2?family=Open+Sans:wght@400;600;700&display=swap" rel="stylesheet">
<style>
  :root {
    --stage-grey: #5e605f;
    --cobalt: #253d8f;
    --white: #ffffff;
    --silver: #c9cacc;
    --silver-line: #9fa3b0;
    --green: #14924a;
    --body-grey: #8d8d8d;
  }
  * { margin: 0; padding: 0; box-sizing: border-box; }
  html, body {
    width: 1200px; height: 1200px; overflow: hidden;
    background: var(--stage-grey);
    font-family: "Open Sans", Arial, sans-serif;
  }
  .stage {
    position: absolute; left: 0; top: 0;
    width: 1500px; height: 1500px;
    transform: scale(0.8); transform-origin: 0 0;
  }
  .carton, .label {
    position: absolute; background: var(--white); overflow: hidden;
  }
  .carton { left: 217px; top: 165px; width: 491px; height: 1127px; }
  .label  { left: 872px; top: 684px; width: 332px; height: 426px; }
  .panel-art { position: absolute; left: 0; top: 0; width: 100%; height: 100%; }
  .brand {
    position: absolute; left: 0; right: 0;
    display: flex; align-items: center; justify-content: center;
    font-weight: 400; white-space: nowrap;
  }
  .brand-dot { border-radius: 50%; border-style: solid; flex: none; }
  .carton .brand--silver { top: 162px; color: var(--silver); font-size: 40px; gap: 16px; }
  .carton .brand--silver .brand-dot { width: 56px; height: 56px; border-width: 3px; border-color: var(--silver); }
  .carton .brand--blue { top: 578px; color: var(--cobalt); font-size: 30px; gap: 12px; }
  .carton .brand--blue .brand-dot { width: 42px; height: 42px; border-width: 3px; border-color: var(--cobalt); }
  .label .brand--blue { top: 82px; color: var(--cobalt); font-size: 17px; gap: 8px; }
  .label .brand--blue .brand-dot { width: 24px; height: 24px; border-width: 2px; border-color: var(--cobalt); }
  .product-name { position: absolute; color: var(--cobalt); line-height: 1; }
  .product-name .line-main { display: block; font-weight: 700; }
  .product-name .line-sub { display: block; font-weight: 400; }
  .carton .product-name { left: 102px; top: 752px; }
  .carton .line-main { font-size: 62px; letter-spacing: 5px; }
  .carton .line-sub { font-size: 40px; letter-spacing: 12px; margin-top: 4px; }
  .label .product-name { left: 63px; top: 176px; }
  .label .line-main { font-size: 46px; letter-spacing: 3px; }
  .label .line-sub { font-size: 30px; letter-spacing: 8px; margin-top: 2px; }
  .details { position: absolute; color: var(--body-grey); }
  .carton .details { left: 106px; top: 872px; font-size: 16px; line-height: 22px; letter-spacing: 1px; }
  .carton .count { display: block; margin-top: 6px; margin-left: -3px; }
  .label .details { left: 67px; top: 265px; font-size: 13px; line-height: 17px; letter-spacing: 0.8px; }
  .label .count { display: block; margin-top: 4px; margin-left: -2px; font-size: 12px; }
  .accent-bar { position: absolute; left: 0; background: var(--green); }
  .carton .accent-bar { top: 999px; width: 373px; height: 13px; }
  .label .accent-bar { top: 346px; width: 266px; height: 13px; }
</style>
</head>
<body>
<main class="stage">

  <section class="carton" aria-label="Carton front panel">
    <svg class="panel-art" viewBox="0 0 491 1127" aria-hidden="true">
      <polygon points="0,0 491,0 491,388 0,540" fill="var(--cobalt)"/>
      <polygon points="13,15 481,15 481,380 13,523" fill="none" stroke="var(--silver-line)" stroke-width="2"/>
    </svg>
    <div class="brand brand--silver"><span class="brand-dot"></span>Verdant Oakfield</div>
    <div class="brand brand--blue"><span class="brand-dot"></span>Verdant Oakfield</div>
    <h1 class="product-name"><span class="line-main">ANXIETY</span><span class="line-sub">SUPPORT</span></h1>
    <p class="details">Lorem ipsum Lorem ipsum-<br>Lorem ipsum Lorem ipsum-<span class="count">30 TABLETS</span></p>
    <div class="accent-bar"></div>
  </section>

  <section class="label" aria-label="Bottle label">
    <svg class="panel-art" viewBox="0 0 332 426" aria-hidden="true">
      <polygon points="0,0 332,0 332,2 0,84" fill="var(--cobalt)"/>
      <polyline points="10,6 10,73 328,2" fill="none" stroke="var(--silver-line)" stroke-width="1.5"/>
    </svg>
    <div class="brand brand--blue"><span class="brand-dot"></span>Verdant Oakfield</div>
    <h2 class="product-name"><span class="line-main">ANXIETY</span><span class="line-sub">SUPPORT</span></h2>
    <p class="details">Lorem ipsum Lorem ipsum-<br>Lorem ipsum Lorem ipsum-<span class="count">30 TABLETS</span></p>
    <div class="accent-bar"></div>
  </section>

</main>
</body>
</html>
```